Wordpress Corporate Website for New Business

We need a corporate website created which will act as a professional shop window for our new business. We do not need special features like merchant facilities or chatbots. The attachment shows suggested key sections as well as some possible wording. Various versions of the company logo have been attached as well to give different options to play with. We are looking for an option which is easy for us to take over and manage moving forward should we need to make minor updates.

Target Market(s)

Corporate entities

Industry/Entity Type

Private share auctions

Coding

Coded - Design and coding required

```html
<!DOCTYPE html>
<html lang="en">
<head>
<meta charset="utf-8">
<title>ShareVeil — Private Share Auctions</title>
<link href="https://fonts.googleapis.com/css2?family=Outfit:wght@500;600;700&family=Inter:wght@400;500;600;700&display=swap" rel="stylesheet">
<style>
:root{
  --purple:#8c0a9c;
  --violet:#5a1aa6;
  --navy:#15068f;
  --deep:#0f0a6c;
  --ink:#1b1740;
  --text:#3c3a52;
  --soft:#f4f2f8;
  --white:#ffffff;
  --band:linear-gradient(100deg,#4b1ca2 0%,#7a0f9e 55%,#8e089a 100%);
}
*{box-sizing:border-box;margin:0;padding:0}
html,body{width:1200px;height:5333px;overflow:hidden;background:var(--white)}
body{font-family:"Inter",sans-serif;color:var(--text)}
.canvas{position:relative;width:1200px;height:5333px;overflow:hidden}
.abs{position:absolute}
h1,h2,h3{font-family:"Outfit",sans-serif;color:var(--ink)}
.btn{position:absolute;display:flex;align-items:center;justify-content:center;gap:8px;background:var(--purple);color:var(--white);font-weight:600;font-size:15px;border-radius:30px;box-shadow:0 0 0 4px rgba(140,10,156,.18)}
.btn .dot{width:11px;height:11px;border-radius:50%;background:var(--white);position:relative}
.btn .dot::after{content:"";position:absolute;left:3px;top:3px;border:3px solid transparent;border-left:4px solid var(--purple)}
.photo{position:absolute}

/* header + hero */
.hero{position:absolute;left:0;top:0;width:1200px;height:660px;background:linear-gradient(90deg,#f7f3fa 0%,#f2f0f6 60%,#f2f2f4 100%)}
.brand{position:absolute;display:flex;align-items:center;gap:10px;font-family:"Outfit",sans-serif;font-weight:700;color:var(--purple)}
.brand .mark{border-radius:50%;background:var(--purple)}
.nav{position:absolute;left:320px;top:36px;display:flex;gap:31px;font-size:15px;font-weight:500;color:var(--ink)}
.nav .active{color:var(--purple)}
.hero-title{position:absolute;left:83px;top:248px;font-size:58px;line-height:60px;font-weight:700}

/* about */
.about h2{position:absolute;left:718px;top:800px;font-size:52px;font-weight:600;white-space:nowrap}
.about h2 span{color:var(--purple)}
.about p{position:absolute;left:720px;top:866px;width:390px;font-size:14.5px;line-height:27px;text-align:justify}

/* team */
.team{position:absolute;left:0;top:1260px;width:1200px;height:648px;background:var(--band);border-top-right-radius:160px}
.team h2,.why h2{color:var(--white);text-align:center;font-weight:600}
.team h2{position:absolute;left:0;right:0;top:56px;font-size:52px}
.team .lead{position:absolute;left:320px;width:560px;top:125px;color:var(--white);font-size:14.5px;font-weight:500;line-height:25px;text-align:center}
.member{position:absolute;top:180px;width:300px;text-align:center;color:var(--white)}
.member .name{position:absolute;top:358px;width:100%;font-weight:700;font-size:17px;letter-spacing:.3px}
.member .role{position:absolute;top:386px;width:100%;font-size:13px;color:rgba(255,255,255,.75)}
.arrow{position:absolute;top:1625px}

/* features */
.features h2{position:absolute;left:0;right:0;top:1975px;text-align:center;font-size:54px;font-weight:600}
.feature h3{position:absolute;font-size:20px;font-weight:600}
.feature p{position:absolute;font-size:14.5px;line-height:25px;width:215px}

/* why */
.why{position:absolute;left:0;top:2525px;width:1200px;height:1025px;background:var(--band);border-top-left-radius:130px}
.why h2{position:absolute;left:0;right:0;top:70px;font-size:54px}
.reason{position:absolute;width:326px;height:326px;border-radius:50%;background:rgba(255,255,255,.14);border:1px solid rgba(255,255,255,.35);color:var(--white);text-align:center}
.reason svg{position:absolute;left:128px;top:18px}
.reason h3{position:absolute;top:106px;width:100%;color:var(--white);font-size:21px;font-weight:600}
.reason p{position:absolute;top:138px;left:34px;right:34px;font-size:14px;line-height:24.5px}

/* faq */
.eyebrow{position:absolute;left:0;right:0;top:3620px;text-align:center;font-size:14px;font-weight:700;color:var(--purple)}
.faq h2{position:absolute;left:0;right:0;top:3636px;text-align:center;font-size:52px;font-weight:600}
.qa{position:absolute;left:196px;width:807px;border:1.5px solid #cfc4e2;border-radius:6px;background:var(--white)}
.qa .q{position:absolute;left:26px;top:18px;font-weight:600;font-size:16px;color:var(--ink)}
.qa .a{position:absolute;left:26px;top:57px;width:690px;font-size:13px;line-height:22px;color:#55536a}
.qa .toggle{position:absolute;right:30px;top:20px;width:24px;height:24px;border-radius:50%;background:var(--purple)}
.qa .toggle::before,.qa .toggle::after{content:"";position:absolute;left:7px;top:11px;width:10px;height:2px;background:var(--white)}
.qa .toggle.plus::after{transform:rotate(90deg)}
.qa .toggle.minus::after{display:none}

/* reach */
.reach{position:absolute;left:0;top:4228px;width:1200px;height:124px;background:var(--band);display:flex;align-items:center;justify-content:center;gap:16px;color:var(--white);font-family:"Outfit",sans-serif;font-size:37px;font-weight:600}
.reach a{color:var(--white);font-weight:400;text-decoration:underline;text-underline-offset:6px}

/* contact */
.contact-card{position:absolute;left:85px;top:4500px;width:465px;height:320px;background:var(--soft);border-radius:28px;border:1px solid #e2def0}
.contact-card h2{position:absolute;left:25px;top:50px;font-size:32px;font-weight:600}
.contact-card p{position:absolute;left:25px;top:100px;width:405px;font-size:14.5px;line-height:24px}
.contact-line{position:absolute;left:25px;display:flex;align-items:center;gap:10px;font-size:14.5px}
.follow{position:absolute;left:25px;top:270px;display:flex;align-items:center;gap:14px;font-weight:700;font-size:18px;color:var(--ink)}
.follow i{width:20px;height:20px;border-radius:3px;background:var(--navy);display:block}

/* footer */
.footer{position:absolute;left:0;top:4952px;width:1200px;height:381px;background:var(--deep);color:rgba(255,255,255,.88)}
.footer h4{position:absolute;top:80px;color:#c53bd6;font-size:19px;font-weight:600}
.footer p{position:absolute;left:85px;top:120px;width:270px;font-size:14.5px;line-height:27px}
.links{position:absolute;top:120px;font-size:14.5px;line-height:40px}
.links li{list-style:none}
.links li::before{content:"› ";}
.social{position:absolute;top:185px;width:44px;height:44px;border-radius:50%;border:2px dashed rgba(255,255,255,.8)}
.legal{position:absolute;top:340px;font-size:14px}
</style>
</head>
<body>
<div class="canvas">

  <!-- Hero -->
  <section class="hero">
    <div class="photo" role="img" aria-label="Business presenter addressing a boardroom meeting with large brand arcs" style="left:540px;top:60px;width:660px;height:600px;background:linear-gradient(135deg,#e9e6ef 0%,#c9c4d6 40%,#6b5c8c 70%,#2a2a3c 100%);clip-path:polygon(20% 0,100% 0,100% 100%,0 100%,5% 60%)"></div>
    <svg class="abs" style="left:0;top:530px" width="160" height="150" viewBox="0 0 160 150"><path d="M14 40 A120 120 0 0 0 150 140" fill="none" stroke="var(--navy)" stroke-width="30"/></svg>
    <h1 class="hero-title">Retain Control,<br>Unlock Liquidity</h1>
    <div class="btn" style="left:85px;top:395px;width:176px;height:48px">Get Started <span class="dot"></span></div>
  </section>

  <header>
    <div class="brand" style="left:85px;top:26px;font-size:34px"><span class="mark" style="width:30px;height:30px"></span>ShareVeil</div>
    <nav class="nav">
      <span class="active">Home</span><span>About</span><span>Our Team</span><span>Key Features</span><span>Why Choose Us</span><span>Support</span>
    </nav>
    <div class="btn" style="left:958px;top:22px;width:156px;height:50px">Contact <span class="dot"></span></div>
  </header>

  <!-- About -->
  <section class="about">
    <div class="photo" role="img" aria-label="Trader working at a desk with charts on multiple monitors" style="left:185px;top:760px;width:450px;height:400px;background:linear-gradient(135deg,#2a3140 0%,#5a6478 45%,#c8ccd6 100%);border-radius:0 0 240px 240px / 0 0 220px 220px"></div>
    <svg class="abs" style="left:440px;top:900px" width="210" height="300" viewBox="0 0 210 300"><path d="M170 10 A180 180 0 0 1 30 280" fill="none" stroke="var(--navy)" stroke-width="26"/></svg>
    <h2>About <span>Share Veil</span></h2>
    <p>At ShareVeil, we empower private companies to take control of their share transactions without the hassle of third-party involvement. Our innovative share exchange platform is designed to connect pre-approved buyers</p>
    <div class="btn" style="left:720px;top:1026px;width:175px;height:50px">Read More <span class="dot"></span></div>
  </section>

  <!-- Team -->
  <section class="team">
    <h2>Our Team</h2>
    <p class="lead">Lorem ipsum dolor sit amet, consectetur adipiscing elit. Duis sit amet tempus urna, eget consequat mi. In eget felis est</p>
    <div class="member" style="left:112px">
      <svg class="abs" style="left:20px;top:40px" width="260" height="270" viewBox="0 0 260 270"><path d="M40 160 A110 110 0 0 0 190 260" fill="none" stroke="var(--white)" stroke-width="24"/><path d="M150 20 A100 100 0 0 1 245 110" fill="none" stroke="var(--white)" stroke-width="24"/></svg>
      <div class="photo" role="img" aria-label="Team member portrait" style="left:58px;top:48px;width:180px;height:220px;background:linear-gradient(180deg,#9a8fb8 0%,#2c3350 100%);border-radius:90px 90px 0 0"></div>
      <div class="name">DANIEL REYES</div><div class="role">CEO</div>
    </div>
    <div class="member" style="left:450px">
      <svg class="abs" style="left:20px;top:40px" width="260" height="270" viewBox="0 0 260 270"><path d="M40 160 A110 110 0 0 0 190 260" fill="none" stroke="var(--white)" stroke-width="24"/><path d="M150 20 A100 100 0 0 1 245 110" fill="none" stroke="var(--white)" stroke-width="24"/></svg>
      <div class="photo" role="img" aria-label="Team member portrait" style="left:58px;top:48px;width:180px;height:220px;background:linear-gradient(180deg,#a794c0 0%,#efe9f3 100%);border-radius:90px 90px 0 0"></div>
      <div class="name">CLARA MORGAN</div><div class="role">CEO</div>
    </div>
    <div class="member" style="left:788px">
      <svg class="abs" style="left:20px;top:40px" width="260" height="270" viewBox="0 0 260 270"><path d="M40 160 A110 110 0 0 0 190 260" fill="none" stroke="var(--white)" stroke-width="24"/><path d="M150 20 A100 100 0 0 1 245 110" fill="none" stroke="var(--white)" stroke-width="24"/></svg>
      <div class="photo" role="img" aria-label="Team member portrait" style="left:58px;top:48px;width:180px;height:220px;background:linear-gradient(180deg,#9a8fb8 0%,#1d1f2e 100%);border-radius:90px 90px 0 0"></div>
      <div class="name">OWEN HARTLEY</div><div class="role">CEO</div>
    </div>
  </section>
  <svg class="abs" style="left:995px;top:1225px" width="205" height="160" viewBox="0 0 205 160"><path d="M8 22 A180 180 0 0 1 190 150" fill="none" stroke="var(--navy)" stroke-width="30"/></svg>
  <svg class="arrow" style="left:85px" width="20" height="36" viewBox="0 0 20 36"><path d="M16 2 L3 18 L16 34" fill="none" stroke="#fff" stroke-width="2"/></svg>
  <svg class="arrow" style="left:1093px" width="20" height="36" viewBox="0 0 20 36"><path d="M4 2 L17 18 L4 34" fill="none" stroke="#fff" stroke-width="2"/></svg>

  <!-- Key Features -->
  <section class="features">
    <h2>Key Features</h2>
    <div class="feature">
      <svg class="abs" style="left:82px;top:2100px" width="250" height="250" viewBox="0 0 250 250"><path d="M128 18 A100 100 0 0 1 225 115" fill="none" stroke="var(--navy)" stroke-width="24"/><path d="M12 125 A112 112 0 0 0 100 240" fill="none" stroke="var(--navy)" stroke-width="24"/></svg>
      <div class="photo" role="img" aria-label="Glass office towers seen from below" style="left:125px;top:2145px;width:165px;height:165px;border-radius:50%;background:linear-gradient(160deg,#f2d8a8 0%,#6b7a8e 50%,#1e2736 100%)"></div>
      <h3 style="left:355px;top:2135px">Company</h3>
      <p style="left:355px;top:2165px">This might explain what we do to help the company roll this out and the process,</p>
      <div class="btn" style="left:355px;top:2253px;width:167px;height:47px">Read More <span class="dot"></span></div>
    </div>
    <div class="feature">
      <svg class="abs" style="left:620px;top:2100px" width="250" height="250" viewBox="0 0 250 250"><path d="M128 18 A100 100 0 0 1 225 115" fill="none" stroke="var(--navy)" stroke-width="24"/><path d="M12 125 A112 112 0 0 0 100 240" fill="none" stroke="var(--navy)" stroke-width="24"/></svg>
      <div class="photo" role="img" aria-label="Shareholder reviewing a laptop in an office" style="left:663px;top:2145px;width:165px;height:165px;border-radius:50%;background:linear-gradient(160deg,#dfe6ea 0%,#7a8a92 50%,#23303a 100%)"></div>
      <h3 style="left:892px;top:2135px">Shareholder</h3>
      <p style="left:892px;top:2165px">Example of the login process, what features the platform</p>
      <div class="btn" style="left:892px;top:2253px;width:167px;height:47px">Read More <span class="dot"></span></div>
    </div>
  </section>

  <!-- Why Choose -->
  <section class="why">
    <h2>Why Choose ShareVeil</h2>
    <div class="reason" style="left:90px;top:215px">
      <svg width="72" height="72" viewBox="0 0 72 72" fill="none" stroke="#fff" stroke-width="2.5"><circle cx="36" cy="36" r="30"/><circle cx="36" cy="34" r="17"/><circle cx="36" cy="34" r="8"/><path d="M26 60 h20"/></svg>
      <h3>Retain Control</h3>
      <p>Companies can maintain control over who participates in their auctions. This control is essential for preserving the company's culture, protecting sensitive information, and ensuring that only pre-approved parties are involved.</p>
    </div>
    <div class="reason" style="left:437px;top:215px">
      <svg width="72" height="72" viewBox="0 0 72 72" fill="none" stroke="#fff" stroke-width="2.5"><circle cx="36" cy="10" r="6"/><path d="M36 16 v50 M8 66 h56 M14 46 h14 v14 h-14z M44 46 h14 v14 h-14z M30 30 h12 v10 h-12z"/></svg>
      <h3>Unlock Liquidity</h3>
      <p>ShareVeil provides a structured marketplace which facilitates efficient and easy share transactions, creating a level of liquidity not previously experienced by private company investors.</p>
    </div>
    <div class="reason" style="left:784px;top:215px">
      <svg width="72" height="72" viewBox="0 0 72 72" fill="none" stroke="#fff" stroke-width="3"><circle cx="36" cy="36" r="30"/><path d="M20 30 h32 l-8 -8 M52 42 h-32 l8 8"/></svg>
      <h3>Direct Transactions</h3>
      <p>Say goodbye to intermediaries. Our platform enables shareholders in private companies to trade shares directly, ensuring transparency and efficiency in every transaction.</p>
    </div>
    <div class="reason" style="left:90px;top:610px">
      <svg width="72" height="72" viewBox="0 0 72 72" fill="none" stroke="#fff" stroke-width="2.5"><path d="M16 6 h30 l12 12 v48 h-42z M22 20 h20 M22 28 h26"/><rect x="28" y="44" width="16" height="14" rx="2"/><path d="M31 44 v-5 a5 5 0 0 1 10 0 v5"/></svg>
      <h3>Secure and Confidential</h3>
      <p>We understand the importance of privacy. Our security measures safeguard your sensitive information, providing a secure space for seamless share trading.</p>
    </div>
    <div class="reason" style="left:437px;top:610px">
      <svg width="72" height="72" viewBox="0 0 72 72" fill="none" stroke="#fff" stroke-width="2.5"><circle cx="36" cy="36" r="30"/><circle cx="36" cy="36" r="22"/><ellipse cx="36" cy="36" rx="10" ry="22"/><path d="M14 36 h44 M18 26 h36 M18 46 h36"/></svg>
      <h3>Global Reach</h3>
      <p>Our platform allows companies and investors from around the world to connect and engage in share auctions effortlessly, no matter where they are located.</p>
    </div>
    <div class="reason" style="left:784px;top:610px">
      <svg width="72" height="72" viewBox="0 0 72 72" fill="none" stroke="#fff" stroke-width="2.5"><rect x="8" y="40" width="24" height="24"/><rect x="26" y="8" width="38" height="38" stroke-dasharray="6 5"/><path d="M34 38 l16 -16 M40 22 h10 v10"/></svg>
      <h3>Scalability</h3>
      <p>The ShareVeil platform can scale to accommodate the needs of companies of varying sizes, from startups to well-established enterprises.</p>
    </div>
  </section>
  <svg class="abs" style="left:0;top:2495px" width="200" height="160" viewBox="0 0 200 160"><path d="M15 150 A150 150 0 0 1 195 18" fill="none" stroke="var(--navy)" stroke-width="30"/></svg>

  <!-- FAQ -->
  <section class="faq">
    <div class="eyebrow">FAQ</div>
    <h2>Have any Questions?</h2>
    <div class="qa" style="top:3718px;height:147px"><span class="q">What&nbsp; placerat felis eu ligula egestas, vulputate elementum?</span><span class="toggle minus"></span>
      <p class="a">Praesent quis congue leo. Nam placerat felis eu ligula egestas, vulputate elementum enim tristique. Donec maximus mi ac rhoncus tempus. Class aptent taciti sociosqu ad litora torquent per conubia nostra, per inceptos himenaeos. Phasellus lun eleifend dolor porttitor.</p></div>
    <div class="qa" style="top:3885px;height:60px"><span class="q">Who pellentesque tristique eu turpis id consectetur?</span><span class="toggle plus" style="top:17px"></span></div>
    <div class="qa" style="top:3957px;height:60px"><span class="q">Why turpis id consectetur?</span><span class="toggle plus" style="top:17px"></span></div>
    <div class="qa" style="top:4028px;height:60px"><span class="q">What feugiat auctor urna a et malesuada fames?</span><span class="toggle plus" style="top:17px"></span></div>
    <div class="qa" style="top:4100px;height:60px"><span class="q">Who pellentesque tristique eu turpis id consectetur?</span><span class="toggle plus" style="top:17px"></span></div>
  </section>

  <!-- Reach -->
  <section class="reach">
    <span>Feel free to reach out to</span>
    <svg width="38" height="28" viewBox="0 0 38 28" fill="none" stroke="#fff" stroke-width="2.5"><rect x="2" y="2" width="34" height="24" rx="3"/><path d="M2 4 l17 13 l17 -13"/></svg>
    <a>info@shareveil.com</a>
  </section>

  <!-- Contact -->
  <section class="contact">
    <div class="contact-card">
      <h2>Contact Us</h2>
      <p>Lorem ipsum dolor sit amet, consectetur adipiscing elit, sed do eiusmod tempor incididunt ut labore et dolore magna aliqua.</p>
      <div class="contact-line" style="top:188px"><svg width="16" height="16" viewBox="0 0 16 16"><path d="M3 1 l3 0 l1 4 l-2 1.5 a9 9 0 0 0 4.5 4.5 l1.5 -2 l4 1 l0 3 a2 2 0 0 1 -2 2 a13 13 0 0 1 -12 -12 a2 2 0 0 1 2 -2z" fill="var(--navy)"/></svg>+65 9000 4821</div>
      <div class="contact-line" style="top:222px"><svg width="16" height="12" viewBox="0 0 16 12"><rect width="16" height="12" rx="1.5" fill="var(--navy)"/><path d="M1 1 l7 5 l7 -5" fill="none" stroke="#fff" stroke-width="1.3"/></svg>info@shareveil.com</div>
      <div class="follow">Follow Us <i></i></div>
    </div>
    <svg class="abs" style="left:440px;top:4480px" width="150" height="110" viewBox="0 0 150 110"><path d="M10 18 A120 120 0 0 1 135 100" fill="none" stroke="var(--navy)" stroke-width="26"/></svg>
    <svg class="abs" style="left:45px;top:4760px" width="140" height="110" viewBox="0 0 140 110"><path d="M18 10 A110 110 0 0 0 130 92" fill="none" stroke="var(--navy)" stroke-width="26"/></svg>
    <svg class="abs" style="left:600px;top:4410px" width="510" height="510" viewBox="0 0 510 510"><path d="M230 20 A225 225 0 0 1 470 180" fill="none" stroke="var(--purple)" stroke-width="34"/><path d="M40 380 A225 225 0 0 0 230 490" fill="none" stroke="var(--navy)" stroke-width="34"/></svg>
    <div class="photo" role="img" aria-label="Two business partners shaking hands in front of trading screens" style="left:615px;top:4440px;width:480px;height:420px;border-radius:50%;background:linear-gradient(135deg,#d9dbe3 0%,#7d8597 45%,#2a2d3c 100%)"></div>
  </section>

  <!-- Footer -->
  <footer class="footer">
    <svg class="abs" style="left:1000px;top:-30px" width="200" height="150" viewBox="0 0 200 150"><path d="M10 18 A170 170 0 0 1 190 140" fill="none" stroke="var(--purple)" stroke-width="30"/></svg>
    <h4 style="left:85px">About Us</h4>
    <p>At ShareVeil, we empower private companies to take control of their share transactions without the hassle of third-party involvement.</p>
    <h4 style="left:460px">Quick Links</h4>
    <ul class="links" style="left:460px"><li>Home</li><li>About</li><li>Our Team</li><li>Key Features</li></ul>
    <ul class="links" style="left:598px"><li>Why Choose Us</li><li>Support</li><li>Contact</li></ul>
    <div class="brand" style="left:865px;top:110px;font-size:44px;color:var(--white)"><span class="mark" style="width:36px;height:36px;background:var(--white)"></span>ShareVeil</div>
    <span class="social" role="img" aria-label="Social profile" style="left:873px"></span>
    <span class="social" role="img" aria-label="Social profile" style="left:952px"></span>
    <span class="social" role="img" aria-label="Social profile" style="left:1030px"></span>
    <span class="legal" style="left:85px">© 2023 <b style="color:#fff">Share Veil</b>. All right reserved</span>
    <span class="legal" style="left:890px">November08, 2023. Layout_4</span>
  </footer>

</div>
</body>
</html>
```